One page template design

Hi creative designer, I want one single page template to use on my newly formed company.

The design most be built around the company logo (see tolvanet.com) and I would like to focus this layout around the top bar and the footer. The middle should be simple and clean for I need to use it with different pages with different functionalities.

The homepage will be used to promote services but on the footer I will place links to our online tools and future internal projects and documentations.

For the homepage I'd like to see well aligned boxes where the products and services will be places. Each project will have a logo (which you don't need to design, but the page layout should have spaces to put them on).

Many thanks.

```html
<!DOCTYPE html>
<html lang="en">
<head>
<meta charset="utf-8">
<title>Tolvanet</title>
<link href="https://fonts.googleapis.com/css2?family=Fredoka:wght@600&family=Questrial&family=Open+Sans:wght@400;600;700&display=swap" rel="stylesheet">
<style>
  :root {
    --sky-top: #6cc6f6;
    --sky-bottom: #7d9ff6;
    --panel: rgba(255, 255, 255, 0.2);
    --heading: #ffffff;
    --heading-shadow: rgba(20, 40, 90, 0.55);
    --body-text: #5d6f8e;
    --button-top: #eef3fb;
    --button-bottom: #a9b4c4;
    --button-text: #454a52;
    --logo: #d3233f;
    --tagline: #5c6272;
    --grass-top: #7fb33a;
    --grass-bottom: #3f6e1c;
    --soil-top: #2c1a0b;
    --soil-bottom: #6a4622;
    --footer-panel: rgba(0, 0, 0, 0.18);
    --footer-box: rgba(0, 0, 0, 0.38);
    --footer-title: #ffffff;
    --footer-sub: #bca58a;
    --footer-muted: #7b6650;
    --footer-link: #e1d2bb;
    --blog-tab: #8d6b48;
    --envelope-blue: #2a4c8a;
  }
  * { box-sizing: border-box; margin: 0; padding: 0; }
  html, body { width: 1046px; height: 1200px; overflow: hidden; }
  body {
    position: relative;
    font-family: "Questrial", sans-serif;
    background: linear-gradient(180deg, var(--sky-top) 0%, var(--sky-bottom) 66%, var(--soil-top) 71%, var(--soil-bottom) 100%);
  }
  .abs { position: absolute; }

  .logo {
    left: 112px; top: 50px;
    font-family: "Fredoka", sans-serif; font-weight: 600;
    font-size: 82px; line-height: 1;
    color: var(--logo);
  }
  .tagline {
    left: 115px; top: 152px;
    font-size: 20px; color: var(--tagline);
  }

  .service {
    position: absolute;
    background: var(--panel);
    border-radius: 7px;
  }
  .service-title {
    position: absolute; left: 13px;
    font-family: "Fredoka", sans-serif; font-weight: 600;
    font-size: 25.5px; text-transform: uppercase;
    color: var(--heading);
    text-shadow: 1px 2px 2px var(--heading-shadow);
    white-space: nowrap;
  }
  .service-text {
    position: absolute; left: 15px;
    font-size: 19px; letter-spacing: 0.3px;
    color: var(--body-text); white-space: nowrap;
  }
  .button {
    position: absolute;
    width: 198px; height: 41px;
    border-radius: 8px;
    background: linear-gradient(180deg, var(--button-top) 0%, #d6deea 48%, var(--button-bottom) 100%);
    box-shadow: 0 2px 3px rgba(30, 50, 90, 0.35);
    font-family: "Open Sans", sans-serif; font-weight: 600;
    font-size: 18px; color: var(--button-text);
    display: flex; align-items: center; justify-content: center;
  }
  .service-logo { position: absolute; border-radius: 10px; }

  .scene {
    left: 0; top: 690px; width: 1046px; height: 171px;
    background: linear-gradient(180deg, rgba(127,179,58,0) 0%, rgba(127,179,58,0) 55%, var(--grass-top) 70%, var(--grass-bottom) 100%);
  }

  .footer-panel { left: 105px; top: 871px; width: 837px; height: 224px; background: var(--footer-panel); border-radius: 6px; }
  .footer-box { position: absolute; background: var(--footer-box); border-radius: 6px; }
  .tools { left: 115px; top: 882px; width: 405px; height: 203px; padding: 7px 13px; }
  .tool-name { font-family: "Open Sans", sans-serif; font-weight: 700; font-size: 22px; color: var(--footer-title); line-height: 26px; text-transform: uppercase; }
  .tool-desc { font-family: "Open Sans", sans-serif; font-size: 14px; color: var(--footer-sub); line-height: 18px; text-transform: uppercase; margin-bottom: 2px; }
  .blog { left: 530px; top: 882px; width: 317px; height: 203px; padding: 8px 14px; }
  .blog-title { font-family: "Open Sans", sans-serif; font-weight: 700; font-size: 22px; color: var(--footer-title); margin-bottom: 6px; }
  .blog-day { font-family: "Open Sans", sans-serif; font-size: 15px; color: var(--footer-link); }
  .blog-text { font-family: "Open Sans", sans-serif; font-size: 13px; line-height: 16px; color: var(--footer-muted); margin-bottom: 14px; padding-right: 20px; }
  .blog-tab { left: 850px; top: 882px; width: 77px; height: 203px; display: flex; align-items: center; justify-content: center; }
  .blog-tab span {
    transform: rotate(90deg); white-space: nowrap;
    font-family: "Fredoka", sans-serif; font-weight: 600; font-size: 32px;
    color: var(--blog-tab); letter-spacing: 2px;
  }

  .copyright { left: 136px; top: 1109px; font-family: "Open Sans", sans-serif; font-weight: 700; font-size: 12px; color: var(--footer-link); }
  .footer-nav { left: 439px; top: 1109px; font-family: "Open Sans", sans-serif; font-weight: 700; font-size: 12.4px; color: var(--footer-link); word-spacing: 1px; }
</style>
</head>
<body>
  <header>
    <div class="abs logo">Tolvanet.com</div>
    <div class="abs tagline">Lorem ipsum doulor sit</div>
  </header>

  <main>
    <section class="service" style="left:112px;top:232px;width:407px;height:134px;">
      <h2 class="service-title" style="top:15px;">Web Development</h2>
      <p class="service-text" style="top:47px;">Lorem ipsum doulor sit amet,</p>
      <div class="button" style="left:12px;top:80px;">Find out More</div>
      <div class="service-logo" role="img" aria-label="Service logo: development" style="left:276px;top:18px;width:100px;height:100px;background:linear-gradient(180deg,#d4dae1,#9aa3ad);"></div>
    </section>

    <section class="service" style="left:528px;top:232px;width:406px;height:134px;">
      <h2 class="service-title" style="top:15px;">Web Design</h2>
      <p class="service-text" style="top:47px;">Lorem ipsum doulor sit amet,</p>
      <div class="button" style="left:12px;top:80px;">Find out More</div>
      <div class="service-logo" role="img" aria-label="Service logo: design" style="left:276px;top:12px;width:112px;height:108px;background:linear-gradient(180deg,#6f8fe6,#a8b0bc);"></div>
    </section>

    <section class="service" style="left:112px;top:377px;width:822px;height:146px;">
      <h2 class="service-title" style="top:9px;">Web Hosting3 Self -Managed Email Package</h2>
      <h2 class="service-title" style="top:44px;">Web Hosting5 Self -Managed Email Package</h2>
      <p class="service-text" style="top:80px;">Duis sagittis tortor eget Lorem ipsum doulor</p>
      <p class="service-text" style="top:109px;left:13px;">Duis sagittis tortor eget&nbsp; risus pulvinar</p>
      <div class="button" style="left:427px;top:91px;">Find out More</div>
      <svg class="service-logo" style="left:683px;top:13px;" width="122" height="122" viewBox="0 0 122 122" aria-label="Email icon" role="img">
        <defs>
          <linearGradient id="envelope-fill" x1="0" y1="0" x2="1" y2="1">
            <stop offset="0" stop-color="#eef3fb"/>
            <stop offset="1" stop-color="#9fb6e0"/>
          </linearGradient>
        </defs>
        <rect x="1.5" y="1.5" width="119" height="119" rx="8" fill="url(#envelope-fill)" stroke="var(--envelope-blue)" stroke-width="3"/>
        <rect x="18" y="29" width="86" height="60" fill="#ffffff" stroke="var(--envelope-blue)" stroke-width="3"/>
        <polyline points="18,29 61,66 104,29" fill="none" stroke="var(--envelope-blue)" stroke-width="3"/>
        <line x1="18" y1="89" x2="49" y2="58" stroke="var(--envelope-blue)" stroke-width="3"/>
        <line x1="104" y1="89" x2="73" y2="58" stroke="var(--envelope-blue)" stroke-width="3"/>
      </svg>
    </section>

    <section class="service" style="left:112px;top:533px;width:407px;height:133px;">
      <h2 class="service-title" style="top:15px;">Domain Registration</h2>
      <p class="service-text" style="top:47px;">Lorem ipsum doulor sit amet,</p>
      <div class="button" style="left:12px;top:82px;">Register Now</div>
      <div class="service-logo" role="img" aria-label="Service logo: domains" style="left:294px;top:29px;width:96px;height:96px;background:linear-gradient(180deg,#6fa6ee,#2a66c8);"></div>
    </section>
  </main>

  <div class="abs scene" role="img" aria-label="Grassy meadow strip with a small mascot and a young plant"></div>

  <footer>
    <div class="abs footer-panel"></div>
    <div class="footer-box tools">
      <div class="tool-name">XML Debugger</div>
      <div class="tool-desc">Free web tool for developers</div>
      <div class="tool-name">Reciprocal Links</div>
      <div class="tool-desc">Online API form for SEO</div>
      <div class="tool-name">IT Resources</div>
      <div class="tool-desc">Web &amp; computing focused directory of links</div>
      <div class="tool-name">Democratic Crawler</div>
      <div class="tool-desc">Crawl sites with this free tool, use wisely!</div>
    </div>
    <div class="footer-box blog">
      <div class="blog-title">BLOG</div>
      <div class="blog-day">Today</div>
      <p class="blog-text">Lorem ipsum doulor sitte amet, consecte tur adipiscing elit. Duis sagittis tortor eget risus pulvinar porttitor.</p>
      <div class="blog-day">Yesterday</div>
      <p class="blog-text">Lorem ipsum doulor sitte amet, consecte tur adipiscing elit. Duis sagittis tortor eget risus pulvinar porttitor.</p>
    </div>
    <div class="footer-box blog-tab"><span>VISIT BLOG</span></div>

    <div class="abs copyright">©2010TolvanetAll rights reserved.</div>
    <nav class="abs footer-nav">About / Site Map /&nbsp; Terms of Service / Privacy Statement / Help Center</nav>
  </footer>
</body>
</html>
```